Stationary Suite for Aussie Law Firm

We are a small law firm operating out of Albany, Western Australia. We have a logo, which we love and was the winner of a ArtHarbor contest last year.
We require a suite of business stationary products incorporating our logo and contact details. These should be:
1. Letterhead (A4)
The letterhead should incorporate the following information in addition to the logo:
ABN 38 902 617 275 (this is our Australian Business Number)
Helena Rusk atf The HTB Family Trust t/as Granite Ridge Law & Settlements (legal name of the business)
Address: Pemberly House, Walcott Street, Albany
Postal Address: PO Box 8170, Albany WA 6332
Telephone: 0491 672 385
Facsimile: 08 9847 2093
Email: info@granitelawgroup.com.au
Website: www.granitelawgroup.com.au
2. Business Card (90mm x 55mm)
I've attached my current business card layout just for your information.
The front of the business card should include the following information in addition to the logo:
Helena Rusk
Director & Principal Solicitor
Telephone: 0491 672 385
Facsimile: 08 9847 2093
Email: helena@granitelawgroup.com.au
The back of the card should be similar to the back of my existing card, but should only have the logo in white and the address of our website (www.granitelawgroup.com.au)
3. Email signature block
This should include the same information as the front of the business card.
4. With Compliments slip (DL size)
The With Compliments slip should include the same information as the Letterhead.
5. Banner (830mm x 2000mm)
We need a banner designed for use at marketing events. This should include our website details and logo - other than that you have fairly free reign with the design.
6. Flyer (DL)
We need a flyer setting out our services and main contact details for use at marketing events. The details to be included are:
Telephone: 0491 672 385
Web: www.granitelawgroup.com.au
Areas of law:
Wills & Estate Planning
Probate & Letters of Administration
Property Law & Conveyancing
General Commercial Law
Business Law
Style guide:
Please look at our website for an idea as to the style of designs we are looking for - www.granitelawgroup.com.au. The design should be modern, sharp and professional.
Colours:
The CMYK details for the colours in our logo are:
Light Blue C72 M5 Y0 K0
Dark Blue C97 M72 Y16 K30
Edit 31/7/2014
I have added a couple of photos that we have used on our website, and additional photos. These are from our local area, so feel free to use these in your designs or to inform them.
- Calibri, Century Gothic

```html
<!DOCTYPE html>
<html lang="en">
<head>
<meta charset="utf-8">
<title>Granite Ridge Law &amp; Settlements — Event Banners</title>
<link rel="stylesheet" href="https://fonts.googleapis.com/css2?family=Questrial&family=Archivo+Narrow:wght@700&display=swap">
<style>
  :root {
    --navy: #0c3b6a;
    --sky: #0cb4e6;
    --sky-text: #3bb6e6;
    --logo-blue: #3fa6db;
    --wave-dark-a: rgba(255,255,255,0.05);
    --wave-dark-b: rgba(255,255,255,0.09);
    --wave-light-a: #f3f8fd;
    --wave-light-b: #e1edf8;
    --white: #ffffff;
    --stage: #e9e6e2;
  }
  * { margin: 0; padding: 0; box-sizing: border-box; }
  html, body {
    width: 1200px; height: 1000px; overflow: hidden;
    background: var(--stage);
  }
  .banner {
    position: absolute;
    top: 85px;
    width: 323px;
    height: 770px;
    overflow: hidden;
    text-align: center;
  }
  .banner--navy { left: 158px; background: var(--navy); }
  .banner--white { left: 685px; background: var(--white); }

  .banner__brand {
    position: absolute;
    top: 228px; left: 40px; right: 40px;
    font-family: "Questrial", "Century Gothic", sans-serif;
    font-size: 21px;
    line-height: 26px;
    letter-spacing: 0.5px;
    text-transform: uppercase;
  }
  .banner--navy .banner__brand { color: var(--white); }
  .banner--white .banner__brand { color: var(--logo-blue); }

  .banner__web {
    position: absolute;
    top: 330px; left: 0; right: 0;
    font-family: "Archivo Narrow", "Arial Narrow", sans-serif;
    font-weight: 700;
    font-size: 27px;
    letter-spacing: -0.3px;
  }
  .banner--navy .banner__web { color: var(--sky-text); }
  .banner--white .banner__web { color: var(--navy); }

  .banner__waves {
    position: absolute;
    top: 345px; left: 0;
    width: 323px; height: 180px;
  }
  .banner--navy .banner__waves {
    background: linear-gradient(170deg, transparent 10%, var(--wave-dark-a) 40%, var(--wave-dark-b) 65%, transparent 95%);
  }
  .banner--white .banner__waves {
    background: linear-gradient(170deg, transparent 10%, var(--wave-light-a) 35%, var(--wave-light-b) 65%, transparent 95%);
  }

  .banner__contact {
    position: absolute;
    top: 522px; left: 0; right: 0;
    font-family: "Questrial", "Century Gothic", sans-serif;
    font-size: 12.5px;
    line-height: 19.7px;
    list-style: none;
  }
  .banner--navy .banner__contact { color: var(--sky-text); }
  .banner--white .banner__contact { color: var(--navy); }

  .banner__footer {
    position: absolute;
    left: 0; bottom: 0;
    width: 100%; height: 140px;
  }
  .banner--navy .banner__footer { background: var(--sky); }
  .banner--white .banner__footer { background: var(--navy); }
</style>
</head>
<body>

<section class="banner banner--navy">
  <div class="banner__brand">Granite Ridge Law &amp; Settlements</div>
  <div class="banner__web">www.granitelawgroup.com.au</div>
  <div class="banner__waves" role="img" aria-label="Soft flowing wave decoration in translucent blue"></div>
  <ul class="banner__contact">
    <li>Pemberly House, Walcott Street, Albany</li>
    <li>Mail&nbsp; PO Box 8170, Albany WA 6332</li>
    <li>Telephone&nbsp; 0491 672 385</li>
    <li>Facsimile&nbsp; 08 9847 2093</li>
    <li>Email&nbsp; info@granitelawgroup.com.au</li>
  </ul>
  <div class="banner__footer"></div>
</section>

<section class="banner banner--white">
  <div class="banner__brand">Granite Ridge Law &amp; Settlements</div>
  <div class="banner__web">www.granitelawgroup.com.au</div>
  <div class="banner__waves" role="img" aria-label="Soft flowing wave decoration in pale blue"></div>
  <ul class="banner__contact">
    <li>Pemberly House, Walcott Street, Albany</li>
    <li>Mail&nbsp; PO Box 8170, Albany WA 6332</li>
    <li>Telephone&nbsp; 0491 672 385</li>
    <li>Facsimile&nbsp; 08 9847 2093</li>
    <li>Email&nbsp; info@granitelawgroup.com.au</li>
  </ul>
  <div class="banner__footer"></div>
</section>

</body>
</html>
```